Etiketten-Design für Trinkweine
Zielgruppe
Wir sind eine Weinkellerei, die einfache Trinkweine für den LEH herstellt.
Unsere Zielgruppen sind Jugendliche .
Wir suchen ein Etikett für unser neues Produkt ,,Traubensaftschorle`` alkoholfrei
Aufgabenstellung
Siehe Anhang , eigene ideen sind auch erwünscht.
Das Etikett sollte Natur verbunden wirken da es ein Bio Produkt ist.
Farben: weiß, grün wären erwünscht.
Das Etikett sollte 75mm hoch und 120mm Breit sein
Strukturpapier weiß
Anbei auch unserer Standartetikett gerne kann das Logo übernommen werden

```html
<!DOCTYPE html>
<html lang="de">
<head>
<meta charset="utf-8">
<title>Traubensaftschorle – Etikett</title>
<link href="https://fonts.googleapis.com/css2?family=Courgette&family=Lexend:wght@300;500&display=swap" rel="stylesheet">
<style>
  :root {
    --paper: #ffffff;
    --stage: #eef0ea;
    --vine: #6a9a35;
    --vine-soft: #b9d394;
    --ink: #111111;
  }
  html, body {
    margin: 0;
    width: 1200px;
    height: 1200px;
    overflow: hidden;
    background: var(--stage);
  }
  .label {
    position: absolute;
    left: 60px;
    top: 262px;
    width: 1080px;
    height: 675px;
    background: var(--paper);
    box-shadow: 0 2px 10px rgba(0,0,0,0.12);
    overflow: hidden;
  }
  .vine-band {
    position: absolute;
    left: 0;
    width: 100%;
  }
  .vine-band--top {
    top: 0;
    height: 105px;
    background: linear-gradient(180deg, var(--vine) 0%, var(--vine-soft) 55%, rgba(255,255,255,0) 100%);
    opacity: 0.75;
  }
  .vine-band--bottom {
    bottom: 0;
    height: 100px;
    background: linear-gradient(0deg, var(--vine) 0%, var(--vine-soft) 55%, rgba(255,255,255,0) 100%);
    opacity: 0.75;
  }
  .brand {
    position: absolute;
    left: 181px;
    top: 40px;
    width: 180px;
    height: 66px;
    border-radius: 50% 50% 0 0;
    background: var(--paper);
    display: flex;
    align-items: center;
    justify-content: center;
    font-family: "Lexend", sans-serif;
    font-weight: 500;
    font-size: 24px;
    color: var(--ink);
    letter-spacing: 0.02em;
  }
  .emblem-frame {
    position: absolute;
    left: 0;
    top: 0;
  }
  .grape-emblem {
    position: absolute;
    left: 228px;
    top: 114px;
    width: 88px;
    height: 122px;
    border-radius: 40% 40% 50% 50%;
    background: radial-gradient(circle at 50% 60%, var(--vine-soft), var(--vine));
    opacity: 0.85;
  }
  .leaf {
    position: absolute;
    top: 470px;
    width: 112px;
    height: 72px;
    border-radius: 50%;
    background: linear-gradient(90deg, var(--vine-soft), var(--vine));
    opacity: 0.8;
  }
  .leaf--left { left: 155px; }
  .leaf--right { left: 285px; transform: scaleX(-1); }
  .product-name {
    position: absolute;
    left: 71px;
    top: 262px;
    width: 400px;
    margin: 0;
    text-align: center;
    font-family: "Courgette", cursive;
    font-weight: 400;
    font-size: 46px;
    line-height: 62px;
    color: var(--ink);
    text-transform: uppercase;
  }
  .volume {
    position: absolute;
    left: 221px;
    top: 522px;
    width: 100px;
    text-align: center;
    font-family: "Courgette", cursive;
    font-size: 22px;
    color: var(--ink);
  }
  .info {
    position: absolute;
    left: 611px;
    width: 400px;
    margin: 0;
    text-align: center;
    font-family: "Lexend", sans-serif;
    font-weight: 300;
    font-size: 29px;
    line-height: 38px;
    color: var(--ink);
  }
  .info--description { top: 160px; }
  .info--lot { top: 306px; }
  .info--bottler { top: 396px; }
</style>
</head>
<body>
  <div class="label">
    <div class="vine-band vine-band--top" role="img" aria-label="Gezeichnete Weinreben und Traubenranken am oberen Rand"></div>
    <div class="vine-band vine-band--bottom" role="img" aria-label="Gezeichnete Weinreben und Traubenranken am unteren Rand"></div>

    <div class="brand">Martin Brauer</div>

    <svg class="emblem-frame" width="540" height="675" viewBox="0 0 540 675" aria-hidden="true">
      <path d="M186 162 A200 200 0 0 0 142 496" fill="none" stroke="var(--vine)" stroke-width="2"/>
      <path d="M356 162 A200 200 0 0 1 400 496" fill="none" stroke="var(--vine)" stroke-width="2"/>
    </svg>

    <div class="grape-emblem" role="img" aria-label="Traube mit Weinblättern als Zeichnung"></div>

    <h1 class="product-name">Trauben<br>Saft<br>Schorle</h1>

    <div class="leaf leaf--left" role="img" aria-label="Gezeichnetes Weinblatt"></div>
    <div class="leaf leaf--right" role="img" aria-label="Gezeichnetes Weinblatt"></div>
    <div class="volume">0,33 L</div>

    <p class="info info--description">Trauben saft&nbsp; mit<br>zugestlew kohlensäure</p>
    <p class="info info--lot">VOS Nr. 01/20</p>
    <p class="info info--bottler">Abfüller: Martin Brauer<br>Rebenweg 14<br>79312 Talheim</p>
  </div>
</body>
</html>
```